Bold Creative Business Card for Digital Marketing Company (Contest)

NOTICE TO DESIGNERS: We understand this is how you make your living. Our commitment to you is to give you awesome and rapid feedback. If we don't think you are on the right track or have a chance of winning we will let you know right away so you don't have to focus your time with us and can continue to get work.

We respect the crowdsource community greatly. We have launched hundreds of crowdsource projects and will make this a great experience for you if you choose to participate (we hope you will!)

--------------
Brief
-------------

We are a cutting edge digital marketing company and we need a new, bold and creative business card designed to reflect who we are and what we do. We want our brand to stand out and be noticed.

The name of our company is: Tanglewood Web Marketing

Definition of Tanglewood:

a. a person pursuing rebellious, even potentially disruptive, policies or ideas:

b. a lone dissenter, as an intellectual, an artist, or a politician, who takes an independent stand apart from his or her associates

c. unorthodox, unconventional, nonconformist

Our businesses is helping small to medium size businesses with their online marketing using bold and creative outside the box strategies that get results.

We are an industry leader and need our business cards to stand out when we hand them out to people, and to be amazing so we stand out and "lead the pack"!

Our current website: http://www.tanglewoodwebmarketing.example

We are rebranding our site to reflect the new logo we just got but you will at least have an idea of who we are and what we do.

Colors We Want: We would like to see burnt Orange, Dark Blue, Gray and/or Black.

We need a front and back designed!

Be creative! Even to the point of creative-shaped business cards. Think outside the box. Let nothing stop your imagination! At the very least, we know that we want business cards that are not the US Standard 2"x3.5"... but rather the wider 3.35"x2.17" (European Standard) with rounded corners if you want to stick with a rectangular shape.

On the front we need:

Our Logo
Place for a name ie Paul Dravecki
Place for our phone number (612) 555 - 8806
Place for email name@tanglewoodwebmarketing.example
Place for our website www.TanglewoodWebMarketing.example

Optional... Place for a headshot photo of the person who the business card will be used for

On the back we need:

The wording... FREE VIDEO SERIES! "12 Bright Moves To Grow Your Business This Week!" www.TanglewoodWebMarketing.example/SmartIdeas

We are excited to see what you come up with.

Thank you for your interests and for participating in this contest!
Updates

Hi everyone! Thanks for all your submissions. However, we feel that most of you are "missing" what we're looking for. Almost all of the designs that have come in are what we would call "standard", "generic", or "typical". We are looking for something creative, different, attention-getting, a business card that would stand out amongst a stack of other business cards. I've shot this video: http://clipviewer.example/t/qWpZtRbHmsd Please take the time to review it. Let us know if you have questions. Thanks!

Target Market(s)

Our target market is small to medium sized business owners who need help with their online marketing.

Industry/Entity Type

Marketing

Font styles to use
Sans Serif

Colors
0355a3
85acd3
f78f20
f37022
faa54b
f68d4d

Requirements
Must have
• On the front we need:

Our Logo

Be CREATIVE! INTERESTING!

On the back we need:

Use the colors from our logo!
Nice to have
• Optional... Place for a headshot photo of the person who the business card will be used for.
Should not have
• Boring, "traditional" look and feel. We want and need to stand out!

```html
<!DOCTYPE html>
<html lang="en">
<head>
<meta charset="utf-8">
<title>Tanglewood Web Marketing – Business Card</title>
<link href="https://fonts.googleapis.com/css2?family=Vollkorn:wght@400;600;700&display=swap" rel="stylesheet">
<style>
  :root {
    --page: #ffffff;
    --ink: #111111;
    --card-dark: #030305;
    --card-light: #ffffff;
    --card-edge: #b9b9b9;
    --brand-blue: #0355a3;
    --brand-orange: #f37022;
    --photo-light: #b9c6d6;
    --photo-dark: #2a3446;
    --shadow: rgba(0, 0, 0, 0.55);
  }
  * { box-sizing: border-box; margin: 0; padding: 0; }
  html, body {
    width: 1200px; height: 1000px; overflow: hidden;
    background: var(--page);
    font-family: "Vollkorn", Georgia, serif;
    font-variant-numeric: lining-nums;
  }
  .canvas { position: relative; width: 1200px; height: 1000px; }

  .card {
    position: absolute; top: 124px; width: 368px; height: 643px;
    border-radius: 18px;
    box-shadow: -7px 7px 8px var(--shadow);
    text-align: center;
  }
  .card--front { left: 294px; background: var(--card-dark); color: #fff; }
  .card--back {
    left: 691px; background: var(--card-light); color: var(--ink);
    border: 1px solid var(--card-edge);
  }

  .brand {
    position: absolute; left: 0; right: 0;
    display: flex; flex-direction: column; align-items: center;
    font-weight: 700; line-height: 1;
  }
  .brand__mark {
    width: 16px; height: 16px; background: var(--brand-orange);
    margin-bottom: 14px;
  }
  .brand__name { letter-spacing: 0.02em; text-transform: uppercase; }
  .brand__tag { font-weight: 400; letter-spacing: 0.3em; margin-top: 4px; }

  .card--front .brand { top: 262px; color: #fff; }
  .card--front .brand__mark { width: 28px; height: 28px; margin-bottom: 28px; }
  .card--front .brand__name { font-size: 41px; }
  .card--front .brand__tag { font-size: 22px; }

  .card--back .brand { top: 70px; color: var(--ink); }
  .card--back .brand__mark { width: 20px; height: 20px; margin-bottom: 20px; }
  .card--back .brand__name { font-size: 27px; }
  .card--back .brand__tag { font-size: 14px; }

  .front__site {
    position: absolute; left: 0; right: 0; top: 598px;
    font-size: 17px; letter-spacing: 0.01em;
  }

  .headshot {
    position: absolute; left: 124px; top: 225px;
    width: 118px; height: 118px; border-radius: 50%;
    border: 3px solid var(--brand-orange);
    padding: 4px; background: var(--card-light);
  }
  .headshot__fill {
    width: 100%; height: 100%; border-radius: 50%;
    background: radial-gradient(circle at 50% 35%, var(--photo-light), var(--photo-dark) 85%);
  }

  .contact { position: absolute; left: 0; right: 0; top: 348px; }
  .contact__name { font-size: 20px; margin-bottom: 7px; }
  .contact__name b { font-weight: 700; }
  .contact__line { font-size: 16px; line-height: 20px; font-weight: 600; }
  .contact__line--email { font-size: 14.6px; }

  .offer { position: absolute; left: 0; right: 0; top: 522px; }
  .offer__rule {
    width: 313px; height: 2px; margin: 0 auto 10px;
    background: var(--brand-blue);
  }
  .offer__title { font-size: 17px; font-weight: 700; line-height: 20px; }
  .offer__quote { font-size: 16px; font-weight: 600; line-height: 20px; }
  .offer__url { font-size: 12.6px; margin-top: 9px; }
</style>
</head>
<body>
<main class="canvas">
  <section class="card card--front" aria-label="Card front">
    <div class="brand">
      <span class="brand__mark"></span>
      <span class="brand__name">Tanglewood</span>
      <span class="brand__tag">web marketing</span>
    </div>
    <p class="front__site">www.tanglewoodwebmarketing.example</p>
  </section>

  <section class="card card--back" aria-label="Card back">
    <div class="brand">
      <span class="brand__mark"></span>
      <span class="brand__name">Tanglewood</span>
      <span class="brand__tag">web marketing</span>
    </div>

    <div class="headshot">
      <div class="headshot__fill" role="img" aria-label="Headshot photo of Paul Dravecki"></div>
    </div>

    <div class="contact">
      <p class="contact__name">Paul <b>Dravecki</b></p>
      <p class="contact__line">(612) 555 - 8806</p>
      <p class="contact__line contact__line--email">paul@tanglewoodwebmarketing.example</p>
    </div>

    <div class="offer">
      <div class="offer__rule"></div>
      <p class="offer__title">FREE VIDEO SERIES!</p>
      <p class="offer__quote">"12 Bright Moves<br>To Grow Your Business This Week!"</p>
      <p class="offer__url">www.TanglewoodWebMarketing.example/BrightMoves</p>
    </div>
  </section>
</main>
</body>
</html>
```